Ferncrest Dental, LLC business card project

Business card to be designed with current logo.
Dental office- please keep design of card that looks clean and professional.
Please include the following info:
Ferncrest Dental, LLC
Dr. Lorna Pettigrew
2871 Marlowe Street
Bethlehem, PA 18093
610-555-0193
ferncrestdental.office@examplemail.test
Hello everyone-
Reason: Just got back from overseas- will look at all designs and provide feedback. Thank you!
Reason: Polling my friends for the final selection-
thank you to all those that participated- so many talented designers!

```html
<!DOCTYPE html>
<html lang="en">
<head>
<meta charset="utf-8">
<title>Ferncrest Dental, LLC – Business Card</title>
<link rel="stylesheet" href="https://fonts.googleapis.com/css2?family=Oxanium:wght@500;600&display=swap">
<style>
  :root {
    --card-bg: #ffffff;
    --ink: #000000;
    --tooth-light: #f4f5f7;
    --tooth-shade: #c9ccd2;
    --brush-blue: #2b4fb3;
  }
  html, body {
    margin: 0;
    padding: 0;
    width: 1200px;
    height: 500px;
    overflow: hidden;
    background: var(--card-bg);
  }
  .card {
    position: relative;
    width: 1200px;
    height: 500px;
    background: var(--card-bg);
    color: var(--ink);
    font-family: "Oxanium", sans-serif;
    font-weight: 600;
    overflow: hidden;
  }
  .card__illustration {
    position: absolute;
    left: 105px;
    top: 40px;
    width: 225px;
    height: 390px;
  }
  .card__line {
    position: absolute;
    margin: 0;
    white-space: nowrap;
    line-height: 1;
  }
  .practice-name {
    left: 375px;
    top: 48px;
    font-size: 68px;
    letter-spacing: 0;
  }
  .dentist-name {
    left: 697px;
    top: 160px;
    transform: translateX(-50%);
    font-size: 50px;
    letter-spacing: 2px;
  }
  .street-address {
    left: 345px;
    top: 242px;
    font-size: 46px;
    letter-spacing: 2px;
  }
  .state-zip {
    left: 495px;
    top: 312px;
    font-size: 40px;
    font-weight: 500;
    letter-spacing: 1px;
  }
  .phone {
    left: 495px;
    top: 372px;
    font-size: 40px;
    font-weight: 500;
    letter-spacing: 1px;
  }
  .email {
    left: 52px;
    top: 444px;
    font-size: 31px;
    font-weight: 500;
  }
</style>
</head>
<body>
  <div class="card">
    <svg class="card__illustration" role="img" aria-label="Illustration of a white tooth with a toothbrush and dental mirror" viewBox="0 0 225 390" xmlns="http://www.w3.org/2000/svg">
      <defs>
        <linearGradient id="toothTone" x1="0" y1="0" x2="1" y2="1">
          <stop offset="0" stop-color="var(--tooth-light)"/>
          <stop offset="0.75" stop-color="var(--tooth-shade)"/>
          <stop offset="1" stop-color="var(--brush-blue)" stop-opacity="0.35"/>
        </linearGradient>
      </defs>
      <rect width="225" height="390" rx="24" fill="url(#toothTone)"/>
    </svg>

    <h1 class="card__line practice-name">Ferncrest Dental, LLC</h1>
    <p class="card__line dentist-name">Dr. Lorna Pettigrew</p>
    <p class="card__line street-address">2871 Marlowe Street Bethlehem</p>
    <p class="card__line state-zip">PA 18093</p>
    <p class="card__line phone">610-555-0193</p>
    <p class="card__line email">E-mail:ferncrestdental.office@examplemail.test</p>
  </div>
</body>
</html>
```